Business Cards- The Manor at Brookridge Golf Club

We would like our business cards to look more high-end. We are a wedding venue that has been in business for 60+ years. We like our logo and our colors - primarily green and a touch of gold/beige. The owner wants our business cards to look more special..

Target Market(s)

Brides who have already toured our venue

Industry/Entity Type

Wedding venue - mansion

Contact Information for Business Card

Name, email, physical address, phone number

Colors
00AB8E
00BBA5
67D7C9
C6EFE9
E9F9F6

Requirements
Must have
• I think we would like our cards to be so pretty that people will want to keep them and will remember the venue. The venue is historic (built in 1850) and beautiful.
Nice to have
• Could we put an image of the building on one side and the contact info on the other?
Should not have
• The color black

```html
<!DOCTYPE html>
<html lang="en">
<head>
<meta charset="utf-8">
<title>The Manor at Brookridge Golf Club — Business Cards</title>
<link rel="stylesheet" href="https://fonts.googleapis.com/css2?family=Sorts+Mill+Goudy&family=Tinos&display=swap">
<style>
  :root {
    --backdrop: #ece6dc;
    --card-white: #ffffff;
    --leaf-green: #7a9b47;
    --leaf-green-light: #8fae5c;
    --teal: #2ea58e;
    --teal-soft: #6cc0ae;
    --gold: #d8c7a4;
    --shadow: rgba(60, 45, 25, 0.35);
  }
  * { margin: 0; padding: 0; box-sizing: border-box; }
  html, body {
    width: 900px; height: 1200px; overflow: hidden;
    background: var(--backdrop);
  }
  .canvas { position: relative; width: 900px; height: 1200px; }

  .card {
    position: absolute; left: 73px; width: 760px; height: 446px;
    border-radius: 40px;
    box-shadow: 4px 6px 14px var(--shadow);
    overflow: hidden;
  }
  .card--front { top: 112px; background: var(--card-white); }
  .card--back  { top: 637px; background: var(--leaf-green); }

  .rule {
    position: absolute; left: 49px; width: 665px; height: 1.5px;
    background: var(--leaf-green-light);
  }
  .rule--top { top: 68px; }
  .rule--bottom { top: 381px; }

  .ornament {
    position: absolute; left: 290px; width: 145px; height: 38px;
    background: linear-gradient(90deg, rgba(122,155,71,0) 0%, rgba(122,155,71,0.35) 30%, rgba(122,155,71,0.55) 50%, rgba(122,155,71,0.35) 70%, rgba(122,155,71,0) 100%);
    border-radius: 19px;
  }
  .ornament--top { top: 26px; }
  .ornament--bottom { top: 385px; }

  .wordmark {
    position: absolute; left: 0; width: 760px;
    display: flex; align-items: center; justify-content: center; gap: 16px;
    font-family: "Sorts Mill Goudy", serif;
    color: var(--leaf-green);
  }
  .card--front .wordmark { top: 112px; }
  .card--back .wordmark { top: 160px; color: var(--card-white); }
  .wordmark__text { text-align: center; line-height: 1; }
  .wordmark__main { display: block; font-size: 66px; }
  .wordmark__sub { display: block; font-size: 25px; margin-top: 6px; }
  .wordmark__mark {
    width: 42px; height: 42px; background: var(--gold);
    flex: none;
  }

  .owner {
    position: absolute; right: 403px; top: 283px; text-align: right;
    font-family: "Sorts Mill Goudy", serif;
  }
  .owner__name { font-size: 25px; color: var(--leaf-green); line-height: 1.2; }
  .owner__title { font-size: 18px; color: var(--teal); margin-top: 4px; }

  .divider {
    position: absolute; left: 381px; top: 274px; width: 1.5px; height: 72px;
    background: var(--leaf-green-light);
  }

  .contact {
    position: absolute; left: 405px; top: 274px; list-style: none;
    font-family: "Tinos", serif; font-size: 15.5px; color: var(--teal);
    line-height: 27px;
  }
  .contact__label { color: var(--teal-soft); }
</style>
</head>
<body>
<main class="canvas">

  <section class="card card--front" aria-label="Business card front">
    <div class="ornament ornament--top" role="img" aria-label="Green scrollwork flourish"></div>
    <div class="rule rule--top"></div>

    <div class="wordmark">
      <div class="wordmark__text">
        <span class="wordmark__main">The Manor</span>
        <span class="wordmark__sub">at Brookridge Golf Club</span>
      </div>
      <span class="wordmark__mark"></span>
    </div>

    <div class="owner">
      <p class="owner__name">Helen Whitaker</p>
      <p class="owner__title">President- Owner</p>
    </div>
    <div class="divider"></div>
    <ul class="contact">
      <li><span class="contact__label">P:</span> (410) 555-0142</li>
      <li><span class="contact__label">E:</span> hwhitaker@brookridgegolfclub.com</li>
      <li>874 Linden Hill Road • Ellwood, MD 21190</li>
    </ul>

    <div class="rule rule--bottom"></div>
    <div class="ornament ornament--bottom" role="img" aria-label="Green scrollwork flourish"></div>
  </section>

  <section class="card card--back" aria-label="Business card back">
    <div class="wordmark">
      <div class="wordmark__text">
        <span class="wordmark__main">The Manor</span>
        <span class="wordmark__sub">at Brookridge Golf Club</span>
      </div>
      <span class="wordmark__mark"></span>
    </div>
  </section>

</main>
</body>
</html>
```